Lantern Across The Gap

Re-design our website www.lanternkv.org
We are a non profit catering for adults, elderly, veterans and youth in impoverished neighborhoods to improve their digital access and help them improve their lives and better our community.

I need the text on home page to stay. Its the first message vsitors shd read when they arrive on our page.

Number of Pages Required

4 page

Font styles to use
Other font styles liked:
• color and font shd be like the image attched below.

```html
<!DOCTYPE html>
<html lang="en">
<head>
<meta charset="utf-8">
<title>Lantern Across The Gap</title>
<link href="https://fonts.googleapis.com/css2?family=Poppins:wght@500;600;700;800&family=Mulish:wght@300;400;600&display=swap" rel="stylesheet">
<style>
:root{
  --blue:#a3c6dc;
  --green:#c8df9b;
  --orange:#f9c999;
  --dark:#2b2b2b;
  --ink:#2e2e2e;
  --muted:#555;
  --light:#f3f3f3;
  --white:#fff;
}
*{margin:0;padding:0;box-sizing:border-box}
html,body{width:1200px;height:2576px;overflow:hidden}
body{position:relative;font-family:"Mulish",sans-serif;color:var(--ink);background:var(--white)}
.abs{position:absolute}
h1,h2,h3,.head{font-family:"Poppins",sans-serif}
a{color:inherit;text-decoration:none}

/* header */
.site-header{position:absolute;left:0;top:0;width:1200px;height:118px;background:var(--white)}
.brand{left:131px;top:28px;width:120px;font-family:"Poppins",sans-serif;font-weight:700;font-size:15px;line-height:18px;color:var(--dark)}
.follow{left:549px;top:33px;font-size:12px;font-weight:600;letter-spacing:.5px}
.social-sq{top:28px;width:25px;height:25px;background:var(--dark);border-radius:3px}
.divider-v{left:805px;top:25px;width:1px;height:36px;background:#bbb}
.call-label{left:819px;top:22px;font-size:12px;font-weight:600}
.call-num{left:819px;top:40px;font-size:18px;font-weight:600;color:var(--dark)}
.btn{display:flex;align-items:center;justify-content:center;font-family:"Poppins",sans-serif;font-weight:600;text-transform:uppercase}
.donate-top{left:971px;top:19px;width:95px;height:41px;background:var(--green);color:var(--white);font-size:14px}
.nav{left:439px;top:73px;display:flex;gap:0;font-size:14px;font-weight:600;letter-spacing:.2px}
.nav a{display:block;height:28px;line-height:28px;padding:0 9px;margin-right:8px}
.nav a.active{background:var(--blue);color:var(--white)}

/* hero */
.hero{left:0;top:118px;width:1200px;height:520px;overflow:hidden}
.hero-photo{position:absolute;inset:0;background:linear-gradient(100deg,#6d6a63 0%,#8a8a84 35%,#9a9993 55%,#5f6150 75%,#b6b5ae 100%)}
.hero-shade{position:absolute;inset:0;background:linear-gradient(90deg,rgba(40,40,40,.55),rgba(40,40,40,0) 60%)}
.welcome{left:160px;top:84px;font-size:30px;font-weight:700;color:var(--blue);letter-spacing:.5px}
.welcome-line{left:163px;top:128px;width:192px;height:4px;background:var(--blue)}
.hero-title{left:160px;top:156px;font-size:50px;line-height:52px;font-weight:800;color:var(--white)}
.hero-btn{left:163px;top:284px;width:134px;height:44px;background:var(--green);color:var(--dark);font-size:14px}
.dots{left:568px;top:436px;display:flex;gap:6px}
.dots span{width:12px;height:12px;border:2px solid var(--white);border-radius:50%}
.dots span.on{background:var(--green)}
.hero-curve{left:0;bottom:0;width:1200px;height:48px}

/* explore */
.explore-title{left:131px;top:686px;width:340px;font-size:29px;line-height:37px;font-weight:700;color:var(--blue)}
.accent{height:3px;width:66px;background:var(--green)}
.explore-text{left:131px;top:891px;width:328px;font-size:14.5px;line-height:20.8px;color:#3a3a3a}
.tile{width:257px;height:183px;display:flex;flex-direction:column;align-items:center;justify-content:flex-end;padding-bottom:30px;text-align:center;font-size:16.5px;line-height:22px;font-weight:600;color:var(--dark);letter-spacing:.3px}
.tile svg{margin-bottom:22px}
.t-green{background:var(--green)}
.t-orange{background:var(--orange)}

/* impact */
.impact{left:0;top:1118px;width:1200px;height:580px;background:var(--blue)}
.impact-photo{left:130px;top:53px;width:422px;height:449px;background:linear-gradient(135deg,#b98b6c 0%,#e2d4c6 40%,#c9b6a3 65%,#8da3b5 100%)}
.impact-title{left:597px;top:40px;width:420px;font-size:29px;line-height:37px;font-weight:700;color:var(--white)}
.impact-sub{left:597px;top:122px;width:440px;font-size:17.5px;line-height:22px;font-weight:600;color:var(--white)}
.impact-line{left:597px;top:188px;width:66px;height:3px;background:var(--white)}
.impact-text{left:597px;top:221px;width:472px;font-size:14px;line-height:19.3px;font-weight:300;color:var(--white)}
.impact-text p+p{margin-top:14px}
.impact-btn{left:597px;top:467px;width:110px;height:35px;background:var(--green);color:var(--white);font-size:12px}

/* e-waste */
.ewaste{left:0;top:1670px;width:1200px;height:566px;background:radial-gradient(circle at 15% 50%,#fbfbfb 0,#f0f0f0 40%,#ececec 100%)}
.ewaste-curve{left:0;top:1668px;width:1200px;height:40px}
.ewaste-title{left:0;top:1724px;width:1200px;text-align:center;font-size:29px;font-weight:700;color:var(--dark)}
.ewaste-line{left:585px;top:1780px}
.card{top:1824px;width:293px;height:368px;background:var(--white);text-align:center;display:flex;flex-direction:column;align-items:center;padding-top:29px}
.card.feature{background:var(--green)}
.card-icon{width:85px;height:85px;border-radius:50%;background:var(--blue);display:flex;align-items:center;justify-content:center}
.feature .card-icon{background:var(--white)}
.card h3{margin-top:25px;font-size:18px;font-weight:700;color:var(--ink)}
.card p{margin-top:16px;width:245px;font-size:13.3px;line-height:19.4px;color:var(--muted)}
.card .btn{position:absolute;top:296px;left:95px;width:103px;height:34px;background:var(--green);color:var(--white);font-size:11.5px}
.feature .btn{background:var(--white);color:var(--green)}

/* footer */
.site-footer{left:0;top:2236px;width:1200px;height:340px;background:var(--dark);color:var(--white)}
.foot-brand{left:131px;top:74px;width:180px;font-family:"Poppins",sans-serif;font-weight:700;font-size:30px;line-height:34px;color:var(--white)}
.foot-col{top:48px}
.foot-col h4{font-family:"Poppins",sans-serif;font-size:14px;font-weight:600;color:var(--green);letter-spacing:.2px}
.foot-col .accent{width:26px;height:2px;margin-top:4px}
.foot-col ul{list-style:none;margin-top:20px;font-size:13.5px;line-height:25.6px}
.foot-donate{left:600px;top:173px;width:95px;height:35px;background:var(--green);color:var(--dark);font-size:14px}
.contact-item{left:870px;display:flex;gap:10px;font-size:12.5px;line-height:16px}
.contact-item .ico{width:22px;height:22px;border-radius:50%;background:var(--white);display:flex;align-items:center;justify-content:center;flex:none;margin-top:4px}
.foot-rule{left:131px;top:252px;width:934px;height:1px;background:#555}
.foot-bottom{top:287px;font-size:13px}
.foot-social{left:458px;top:278px;display:flex;align-items:center;gap:10px;font-size:11px}
.foot-social span.c{width:22px;height:22px;border-radius:50%;background:var(--white)}
.copyright{left:780px;top:289px;font-size:11.5px}
</style>
</head>
<body>

<header class="site-header">
  <div class="abs brand">Lantern Across The Gap</div>
  <div class="abs follow">FOLLOW</div>
  <span class="abs social-sq" style="left:614px"></span>
  <span class="abs social-sq" style="left:646px"></span>
  <span class="abs social-sq" style="left:678px"></span>
  <span class="abs social-sq" style="left:710px"></span>
  <svg class="abs" style="left:762px;top:26px" width="34" height="34" viewBox="0 0 34 34" fill="none" stroke="#6d8ea4" stroke-width="1.6">
    <path d="M6 6c-3 3-1 10 5 16s13 8 16 5l-4-5-4 2c-3-1-7-5-8-8l2-4z"/>
    <circle cx="24" cy="9" r="6"/>
  </svg>
  <span class="abs divider-v"></span>
  <div class="abs call-label">CALL US</div>
  <div class="abs call-num">(555) 214 0188</div>
  <a class="abs btn donate-top">Donate</a>
  <nav class="abs nav">
    <a class="active">HOME</a><a>GET CONNECTED</a><a>E-WASTE SERVICES</a><a>OUR IMPACT</a><a>ABOUT</a><a>CONTACT</a>
  </nav>
</header>

<section class="abs hero">
  <div class="hero-photo" role="img" aria-label="Photo of a veteran in camouflage working on a laptop at home"></div>
  <div class="hero-shade"></div>
  <h2 class="abs welcome">WELCOME TO</h2>
  <span class="abs welcome-line"></span>
  <h1 class="abs hero-title">LANTERN ACROSS<br>THE GAP</h1>
  <a class="abs btn hero-btn">Read More</a>
  <div class="abs dots"><span></span><span class="on"></span><span></span><span></span></div>
  <svg class="abs hero-curve" viewBox="0 0 1200 48" preserveAspectRatio="none">
    <path d="M0 48 Q600 -30 1200 48 Z" fill="#fff"/>
    <path d="M0 40 Q600 -30 1200 40 L1200 48 Q600 -22 0 48 Z" fill="var(--blue)"/>
  </svg>
</section>

<section>
  <h2 class="abs explore-title">Explore Opportunities Online with Low-Cost Technology, Internet, Training &amp; Support</h2>
  <span class="abs accent" style="left:131px;top:854px"></span>
  <p class="abs explore-text">In order to comprehensively shrink the digital divide, we offer you access to low-cost computers, low-cost internet, free digital literacy training and tech support. Click the boxes below to explore how we can help you and members of your community unlock their full potential through digital technology.</p>

  <div class="abs tile t-green" style="left:534px;top:678px">
    <svg width="58" height="58" viewBox="0 0 58 58" fill="none" stroke="#333" stroke-width="1.6"><rect x="3" y="14" width="36" height="26" rx="2"/><rect x="7" y="18" width="28" height="18"/><path d="M16 40v6h10v-6M11 48h20"/><rect x="40" y="4" width="14" height="46" rx="1"/><path d="M43 10h8M43 14h8M43 44h8"/></svg>
    AFFORDABLE<br>TECHNOLOGY
  </div>
  <div class="abs tile t-orange" style="left:811px;top:678px">
    <svg width="56" height="56" viewBox="0 0 56 56" fill="none" stroke="#333" stroke-width="1.6"><circle cx="28" cy="28" r="13"/><path d="M15 28h26M28 15v26M22 18c-4 6-4 14 0 20M34 18c4 6 4 14 0 20"/><circle cx="28" cy="4" r="3"/><circle cx="28" cy="52" r="3"/><circle cx="6" cy="14" r="3"/><circle cx="50" cy="14" r="3"/><circle cx="6" cy="42" r="3"/><circle cx="50" cy="42" r="3"/><path d="M28 7v8M28 41v8M9 16l8 5M47 16l-8 5M9 40l8-5M47 40l-8-5"/></svg>
    INTERNET<br>ACCESS
  </div>
  <div class="abs tile t-orange" style="left:534px;top:883px">
    <svg width="54" height="56" viewBox="0 0 54 56" fill="none" stroke="#333" stroke-width="1.6"><path d="M27 4l4 5 6-2 1 6 6 2-2 6 5 4-5 4 2 6-6 2-1 6-6-2-4 5-4-5-6 2-1-6-6-2 2-6-5-4 5-4-2-6 6-2 1-6 6 2z"/><path d="M21 36c-3-3-5-6-5-10a11 11 0 0 1 22 0c0 4-2 7-5 10v6H21z"/><path d="M22 46h10M24 50h6"/></svg>
    DIGITAL LITERACY<br>TRAINING
  </div>
  <div class="abs tile t-orange" style="left:811px;top:883px">
    <svg width="52" height="56" viewBox="0 0 52 56" fill="none" stroke="#333" stroke-width="1.6"><circle cx="26" cy="20" r="11"/><path d="M12 22v-4a14 14 0 0 1 28 0v4M12 18v8h4M40 18v8h-4v4l-8 3"/><path d="M4 54c0-12 9-18 22-18s22 6 22 18zM20 38l6 8 6-8"/></svg>
    TECH<br>SUPPORT
  </div>
</section>

<section class="abs impact">
  <div class="abs impact-photo" role="img" aria-label="Photo of an older couple smiling while using a laptop together"></div>
  <h2 class="abs impact-title">Creating a Social Impact with e-Waste</h2>
  <p class="abs impact-sub head">by transforming Unwanted Technology into Opportunities for People In-Need.</p>
  <span class="abs impact-line"></span>
  <div class="abs impact-text">
    <p>Lantern Across The Gap is a nonprofit and social enterprise that creates equitable access to opportunity by providing devices, internet access, digital skills training, and tech support for low-income families, the homeless, and Veterans in our communities while at the same time, empowering businesses and organizations to do good by diverting technology from landfills to protect our planet.</p>
    <p>Being digitally literate is no longer a luxury, it is a must-have skill for everyone to manage information, communicate, manage money, and access support plus other government services. It has become an essential tool for modern-day citizenship and participation; no one can afford to be left behind.</p>
  </div>
  <a class="abs btn impact-btn">Read More</a>
</section>

<section>
  <div class="abs ewaste"></div>
  <svg class="abs ewaste-curve" viewBox="0 0 1200 40" preserveAspectRatio="none">
    <path d="M0 0 H1200 V36 Q600 -14 0 30 Z" fill="var(--blue)"/>
    <path d="M0 30 Q600 -14 1200 36 L1200 40 Q600 -8 0 36 Z" fill="var(--orange)"/>
  </svg>
  <h2 class="abs ewaste-title">e-Waste Services</h2>
  <span class="abs accent ewaste-line" style="width:34px"></span>

  <article class="abs card" style="left:133px">
    <div class="card-icon"><svg width="50" height="44" viewBox="0 0 50 44" fill="none" stroke="#fff" stroke-width="2"><rect x="10" y="4" width="30" height="22" rx="2"/><path d="M20 10l9 4-4 1 3 4-2 1-3-4-2 3z" fill="#fff"/><path d="M4 30h42l-4 10H8z"/><path d="M12 34h26M12 37h26"/></svg></div>
    <h3>e-Waste Services</h3>
    <p>Bridging The Gap makes it easy for businesses and organizations across different industries to do good by diverting their unwanted technology away from landfills</p>
    <a class="btn">Read More</a>
  </article>
  <article class="abs card feature" style="left:452px">
    <div class="card-icon"><svg width="54" height="46" viewBox="0 0 54 46" fill="none" stroke="#c8df9b" stroke-width="2"><path d="M14 2h22l6 6v10H14z"/><rect x="4" y="18" width="46" height="12" rx="2"/><path d="M10 24h34M14 30v12M20 30v14M26 30v10M32 30v14M38 30v12"/></svg></div>
    <h3>Data Destruction</h3>
    <p>Data breaches cost companies an average of $4 million per instance and 80% of customers refuse to shop with companies who compromise their data.</p>
    <a class="btn">Read More</a>
  </article>
  <article class="abs card" style="left:775px">
    <div class="card-icon"><svg width="44" height="38" viewBox="0 0 44 38" fill="none" stroke="#fff" stroke-width="2.5"><path d="M8 6h28l6 18v10H2V24z"/><path d="M2 24h40"/><circle cx="10" cy="29" r="1.5" fill="#fff"/><path d="M26 29h10"/></svg></div>
    <h3>Tech Drive</h3>
    <p>By hosting a Tech Drive for people at your organization or in your community, you're helping them safely dispose of unwanted computers and technology.</p>
    <a class="btn">Read More</a>
  </article>
</section>

<footer class="abs site-footer">
  <div class="abs foot-brand">Lantern Across The Gap</div>

  <div class="abs foot-col" style="left:376px">
    <h4>GET CONNECTED</h4><div class="accent"></div>
    <ul><li>Get Technology</li><li>Low-Cost Internet</li><li>Digital Training</li><li>Tech Support</li><li>For Organizations</li></ul>
  </div>
  <div class="abs foot-col" style="left:597px">
    <h4>REPURPOSE YOUR TECH</h4><div class="accent"></div>
    <ul><li>E-Waste Services</li><li>Data Destruction</li><li>Technology Drives</li></ul>
  </div>
  <a class="abs btn foot-donate">Donate</a>

  <div class="abs foot-col" style="left:872px">
    <h4>CONTACT</h4><div class="accent"></div>
  </div>
  <div class="abs contact-item" style="top:92px">
    <span class="ico"><svg width="10" height="13" viewBox="0 0 10 13"><path d="M5 0a5 5 0 0 1 5 5c0 3-5 8-5 8S0 8 0 5a5 5 0 0 1 5-5z" fill="#2b2b2b"/><circle cx="5" cy="5" r="1.8" fill="#fff"/></svg></span>
    <span>418 Harbor View Ave,<br>Kestrel Valley, CA 90211</span>
  </div>
  <div class="abs contact-item" style="top:143px">
    <span class="ico"><svg width="11" height="11" viewBox="0 0 11 11"><path d="M1 1l3 0 1 3-1.5 1c.7 1.3 1.6 2.2 2.5 2.5L7 6l3 1v3c-5 0-9-4-9-9z" fill="#2b2b2b"/></svg></span>
    <span>Call Us<br>(555) 214-0188</span>
  </div>
  <div class="abs contact-item" style="top:195px">
    <span class="ico"><svg width="12" height="9" viewBox="0 0 12 9"><rect width="12" height="9" rx="1" fill="#2b2b2b"/><path d="M0 0l6 5 6-5" stroke="#fff" fill="none"/></svg></span>
    <span>E mail Us<br>hello@lanternkv.org</span>
  </div>

  <span class="abs foot-rule"></span>
  <div class="abs foot-bottom" style="left:131px">PRIVACY &amp; SECURITY POLICY</div>
  <div class="abs foot-social">Follow us <span class="c"></span><span class="c"></span><span class="c"></span><span class="c"></span></div>
  <div class="abs copyright">© 2022 by Lantern Across The Gap. All rights reserved.</div>
</footer>

</body>
</html>
```